Brevik Plant Traders Company - Enhance our webpage

We have an existing website - please see www.brockwaytooling.com. The text in there is fundamentally what we want to say. There is also a search function where you can search our database, which is crucial to the site. We are happy with our logo, top left-hand side and want it to remain as it is. Everything else, including pictures, drawings and animation can be changed. In general, the website looks a little tired and the icons on the tabs need creative input.

We want our website to look dynamic, eye-catching, bold, very professional, modern and also uphold our impeccable 30-year reputation in the business.

We are essentially looking for a young, dynamic mind to provide our website with some inspiration. We encourage all designers to use their imagination and surprise us.

We have technical people to do the technical work, such as coding, but what we are looking for is asthetic creativity.

In addition, we have seen our competitors offer a translation service on their website i.e. you can just click on a flag and the website will turn into a different language. If you can incorporate this, it would be very useful.
Updates

Reason: Hi All - we have received some fantastic designs, so thank you. We are extending the deadline so that people can upgrade theirs slightly. We haven't seen enough dynamism with pictures and icons. And for those who have shown dynamism in those departments, we would also like you to consider including a video on the home page of some sort. You can find many videos of working machines like these on Clip-Spool. Thanks.

Target Market(s)

International Engineering companies

Industry/Entity Type

Flag

Requirements
Must have
• The "search database" facility must remain there.
Nice to have
• Perhaps some working videos running on the homepage of some of the types of machines we sell. You can find many such videos on ClipSpool. We will constantly change those as we get new stock in.

```html
<!DOCTYPE html>
<html lang="en">
<head>
<meta charset="utf-8">
<title>Brockway Tooling</title>
<link rel="stylesheet" href="https://fonts.googleapis.com/css2?family=Cinzel:wght@400;700&family=Gelasio:wght@400;600&family=Open+Sans:wght@400;600;700&display=swap">
<style>
:root{
  --ink:#2b2b2b;
  --header:#2e2e2e;
  --nav:#3a3a3a;
  --page:#f1f1f1;
  --panel:#4a4a4a;
  --text:#5a5a5a;
  --light:#e8e8e8;
  --muted:#9a9a9a;
  --red:#c0201e;
  --green:#6fbf3a;
  --field:#ffffff;
}
*{margin:0;padding:0;box-sizing:border-box}
html,body{width:720px;height:1200px;overflow:hidden}
body{background:var(--page);font-family:"Gelasio",Georgia,serif;color:var(--text);position:relative}
.abs{position:absolute}
.top-bar{left:0;top:0;width:720px;height:100px;background:var(--header)}
.util-links{right:95px;top:2px;font:7px "Open Sans",sans-serif;color:#ccc;letter-spacing:.2px}
.util-line{left:0;top:13px;width:720px;border-top:1px dashed #555}
.logo{left:76px;top:22px;font:700 28px "Open Sans",sans-serif;color:#fff;letter-spacing:1px;line-height:1}
.logo small{display:block;font-size:8px;letter-spacing:5px;margin-top:2px}
.call{right:78px;top:62px;font:12px "Open Sans",sans-serif;color:#ddd}
.register{right:78px;top:83px;font:7px "Gelasio",serif;color:#999}
.register .up{color:var(--green)}.register .in{color:#fff}
.nav{left:0;top:100px;width:720px;height:39px;background:var(--nav);display:flex;padding-left:76px;align-items:center;gap:0}
.nav a{font:10.5px "Cinzel",serif;color:#e6e6e6;text-decoration:none;position:relative;margin-right:27px}
.nav a.active::after{content:"";position:absolute;left:50%;bottom:-16px;margin-left:-5px;border:5px solid transparent;border-bottom-color:var(--page)}
.slider{left:74px;top:147px;width:572px;height:287px;background:#3c3c3c;padding:6px}
.slider .stage{position:relative;width:100%;height:100%;overflow:hidden}
.slide-copy{right:11px;top:12px;text-align:right;width:260px}
.slide-copy h2{font:400 42px "Gelasio",serif;color:#fff;line-height:1}
.slide-copy h3{font:400 20px "Gelasio",serif;color:var(--red);line-height:1.05}
.slide-copy p{font:6.4px "Gelasio",serif;color:#fff;line-height:1.15;margin-top:5px;padding-left:110px}
.slide-copy .more{display:block;font:8.5px "Gelasio",serif;color:#fff;margin-top:12px;letter-spacing:.3px}
.dots{left:232px;bottom:-1px;width:100px;height:20px;background:#3c3c3c;border-radius:10px 10px 0 0;display:flex;justify-content:center;align-items:center;gap:4px}
.dots span{width:8px;height:8px;border-radius:50%;background:#fff}
.dots span.on{background:#222}
h2.section{font:400 18px "Gelasio",serif;color:var(--ink)}
.products{left:74px;top:483px;display:flex;gap:15px}
.product{width:132px;height:92px;border:4px solid #444;background:#fff;display:flex;align-items:center;justify-content:center}
.product .shot{width:80px;height:68px;background:linear-gradient(160deg,#c9ccd0,#8b9096 60%,#6a6e73);border-radius:2px;box-shadow:4px 4px 6px rgba(0,0,0,.25)}
.company{left:74px;top:632px;width:409px;font-size:10.4px;line-height:15.6px;text-align:justify}
.company p{margin-bottom:15.6px}
.company .sign{color:var(--ink);font-size:10.4px}
.search{left:510px;top:607px;width:136px;height:244px;background:var(--panel);border-radius:3px;padding:9px 11px}
.search h4{font:400 13px "Gelasio",serif;color:#fff;margin-bottom:6px}
.search label{display:block;font:7.5px "Gelasio",serif;color:#eee;margin-top:8px;margin-bottom:3px}
.search .field{height:17px;background:var(--field);border:1px solid #bbb;position:relative}
.search .go{position:absolute;right:2px;top:2px;width:15px;height:11px;border:1px solid #777;border-radius:2px;background:#ddd}
.search .btn{margin-top:12px;width:52px;height:22px;background:#fff;border:1px solid #ccc;font:7.5px "Gelasio",serif;color:#888;display:flex;align-items:center;justify-content:center}
.footer{left:0;top:962px;width:720px;height:198px;background:var(--header)}
.footer-edge{left:0;top:958px;width:720px;height:6px}
.footer h5{font:600 10px "Open Sans",sans-serif;color:#fff}
.links{font:8px "Open Sans",sans-serif;color:#ddd;list-style:none}
.links li{height:15px;display:flex;align-items:center;gap:5px}
.questions{left:418px;top:997px}
.questions h5{font-size:14px}
.inp{background:#fff;border:1px solid #999;font:8px "Open Sans",sans-serif;color:#444;padding:4px 11px}
.submit{left:418px;top:1131px;width:56px;height:19px;background:#2a2a2a;border:1px solid #666;border-radius:2px;font:8.5px "Open Sans",sans-serif;color:#eee;display:flex;align-items:center;justify-content:center}
.bottom{left:0;top:1160px;width:720px;height:40px;background:linear-gradient(#2b2b2b,#1f1f1f);border-top:1px dashed #555}
.copy{left:72px;top:1178px;font:7.5px "Open Sans",sans-serif;color:#ddd}
.social{left:471px;top:1174px;font:8px "Open Sans",sans-serif;color:#ddd;display:flex;align-items:center;gap:11px}
.social i{display:block;width:13px;height:13px;background:#4a8fd0;border-radius:2px}
</style>
</head>
<body>
<header class="abs top-bar" aria-label="Site header"></header>
<div class="abs util-links">Feedback &nbsp;|&nbsp; About Us &nbsp;|&nbsp; Testimonials &nbsp;|&nbsp; Contact Us</div>
<div class="abs util-line"></div>
<div class="abs logo">Brockway<small>TOOLING</small></div>
<div class="abs call">Call Us At 0100-5550-182</div>
<div class="abs register">You have not yet registered <span class="up">Sign Up</span> Or <span class="in">Log In</span></div>

<nav class="abs nav">
  <a class="active" href="#">Home</a>
  <a href="#">New CNC Machines</a>
  <a href="#">Used Machines</a>
  <a href="#">Manufacturing</a>
  <a href="#">Contact</a>
</nav>

<section class="abs slider">
  <div class="stage">
    <svg width="560" height="275" style="position:absolute;left:0;top:0">
      <rect width="560" height="275" role="img" aria-label="Photograph of an industrial plant lit at night" fill="url(#plant)"/>
      <defs>
        <linearGradient id="plant" x1="0" y1="0" x2="1" y2="1">
          <stop offset="0" stop-color="#2a1a10"/>
          <stop offset=".4" stop-color="#8a4a18"/>
          <stop offset=".7" stop-color="#b8772e"/>
          <stop offset="1" stop-color="#4a2a14"/>
        </linearGradient>
      </defs>
      <polygon points="240,0 560,0 560,220" fill="#2e2e2e" opacity=".95"/>
      <polygon points="330,0 560,0 560,275 520,275" fill="#2e2e2e" opacity=".55"/>
    </svg>
    <div class="abs slide-copy">
      <h2>World-class</h2>
      <h3>CNC Conventional<br>Machine Tools</h3>
      <p>Brockway Tooling is an established vendor of new and used machine tools, with over 30years' experience in buying, rebuild retrofitting and new machine tools. We are a global leader in making of new CNC machines, as we make conventional machines into cheaper CNC machine.</p>
      <span class="more">READ MORE</span>
    </div>
    <div class="abs dots"><span></span><span class="on"></span><span></span><span></span><span></span><span></span></div>
  </div>
</section>

<h2 class="abs section" style="left:79px;top:450px">Products</h2>
<div class="abs products">
  <div class="product"><div class="shot" role="img" aria-label="CNC machine product photo"></div></div>
  <div class="product"><div class="shot" role="img" aria-label="CNC machine product photo"></div></div>
  <div class="product"><div class="shot" role="img" aria-label="CNC machine product photo"></div></div>
  <div class="product"><div class="shot" role="img" aria-label="CNC machine product photo"></div></div>
</div>

<h2 class="abs section" style="left:78px;top:598px">Our Company</h2>
<div class="abs company">
  <p>Brockway Tooling is an established vendor of new and used machine tools, with over 30 years' experience in buying, rebuilding, retrofitting and commissioning machine tools WORLDWIDE. We have industrial space both in London and Mumbai, where we store over 200 machines at any given time. We specialise in gear manufacturing, pressure diecasting, plano miller, boring and grinding machines, as well as heat treatment facilities, machining and turning centres. Such machines find their usage in the automotive, aviation, power generation, mining and construction industries. Our stock includes the industry's best brands such as Garston, Pelham, Hurlow and Bexley. The stock comprises both CNC and conventional machines.</p>
  <p>We are a global leader in the production of new CNC machines, as we retrofit conventional machines into affordable CNC machine tools.</p>
  <p>We also have a gear manufacturing facility in Mumbai, producing quality bespoke gears for some of India's leading Original Equipment Manufacturers. We can produce gears from 16mm to 1600 mm in diameter.</p>
  <p class="sign">BROCKWAY TOOLING</p>
</div>

<aside class="abs search">
  <h4>Search</h4>
  <label>Title</label><div class="field"></div>
  <label>Class</label><div class="field"><span class="go"></span></div>
  <label>Year Made</label><div class="field"><span class="go"></span></div>
  <label>Model</label><div class="field"><span class="go"></span></div>
  <div class="btn">SEARCH</div>
</aside>

<svg class="abs footer-edge" width="720" height="6"><path d="M0 6 L0 3 Q3 0 6 3 T12 3 T18 3 T24 3 T30 3 T36 3 T42 3 T48 3 T54 3 T60 3 T66 3 T72 3 T78 3 T84 3 T90 3 T96 3 T102 3 T108 3 T114 3 T120 3 T126 3 T132 3 T138 3 T144 3 T150 3 T156 3 T162 3 T168 3 T174 3 T180 3 T186 3 T192 3 T198 3 T204 3 T210 3 T216 3 T222 3 T228 3 T234 3 T240 3 T246 3 T252 3 T258 3 T264 3 T270 3 T276 3 T282 3 T288 3 T294 3 T300 3 T306 3 T312 3 T318 3 T324 3 T330 3 T336 3 T342 3 T348 3 T354 3 T360 3 T366 3 T372 3 T378 3 T384 3 T390 3 T396 3 T402 3 T408 3 T414 3 T420 3 T426 3 T432 3 T438 3 T444 3 T450 3 T456 3 T462 3 T468 3 T474 3 T480 3 T486 3 T492 3 T498 3 T504 3 T510 3 T516 3 T522 3 T528 3 T534 3 T540 3 T546 3 T552 3 T558 3 T564 3 T570 3 T576 3 T582 3 T588 3 T594 3 T600 3 T606 3 T612 3 T618 3 T624 3 T630 3 T636 3 T642 3 T648 3 T654 3 T660 3 T666 3 T672 3 T678 3 T684 3 T690 3 T696 3 T702 3 T708 3 T714 3 T720 3 L720 6 Z" fill="#2e2e2e"/></svg>
<footer class="abs footer"></footer>

<h5 class="abs" style="left:72px;top:997px;font:600 10px 'Open Sans',sans-serif;color:#fff">Services</h5>
<ul class="abs links" style="left:77px;top:1018px">
  <li><svg width="9" height="7"><path d="M0 3.5H8M5 1L8 3.5L5 6" stroke="#ddd" fill="none"/></svg>Vestibulum Ante</li>
  <li><svg width="9" height="7"><path d="M0 3.5H8M5 1L8 3.5L5 6" stroke="#ddd" fill="none"/></svg>Sipsum Primis in Faucibus</li>
  <li><svg width="9" height="7"><path d="M0 3.5H8M5 1L8 3.5L5 6" stroke="#ddd" fill="none"/></svg>Orci Luctus et Ultrices</li>
  <li><svg width="9" height="7"><path d="M0 3.5H8M5 1L8 3.5L5 6" stroke="#ddd" fill="none"/></svg>Posuere at Sed Accusom</li>
  <li><svg width="9" height="7"><path d="M0 3.5H8M5 1L8 3.5L5 6" stroke="#ddd" fill="none"/></svg>Magnus Lorem Quisit</li>
  <li><svg width="9" height="7"><path d="M0 3.5H8M5 1L8 3.5L5 6" stroke="#ddd" fill="none"/></svg>Aenean id Dolroest Pursus</li>
  <li><svg width="9" height="7"><path d="M0 3.5H8M5 1L8 3.5L5 6" stroke="#ddd" fill="none"/></svg>Nulla Quam Mollis</li>
</ul>

<h5 class="abs" style="left:246px;top:997px;font:600 10px 'Open Sans',sans-serif;color:#fff">Other Links &amp; Information</h5>
<ul class="abs links" style="left:251px;top:1018px">
  <li><svg width="9" height="7"><path d="M0 3.5H8M5 1L8 3.5L5 6" stroke="#ddd" fill="none"/></svg>Vestibulum Ante</li>
  <li><svg width="9" height="7"><path d="M0 3.5H8M5 1L8 3.5L5 6" stroke="#ddd" fill="none"/></svg>Sipsum Primis in Faucibus</li>
  <li><svg width="9" height="7"><path d="M0 3.5H8M5 1L8 3.5L5 6" stroke="#ddd" fill="none"/></svg>Orci Luctus et Ultrices</li>
  <li><svg width="9" height="7"><path d="M0 3.5H8M5 1L8 3.5L5 6" stroke="#ddd" fill="none"/></svg>Posuere at Sed Accusom</li>
  <li><svg width="9" height="7"><path d="M0 3.5H8M5 1L8 3.5L5 6" stroke="#ddd" fill="none"/></svg>Magnus Lorem Quisit</li>
  <li><svg width="9" height="7"><path d="M0 3.5H8M5 1L8 3.5L5 6" stroke="#ddd" fill="none"/></svg>Aenean id Dolroest Pursus</li>
  <li><svg width="9" height="7"><path d="M0 3.5H8M5 1L8 3.5L5 6" stroke="#ddd" fill="none"/></svg>Nulla Quam Mollis</li>
</ul>

<h5 class="abs" style="left:418px;top:996px;font:700 14px 'Open Sans',sans-serif;color:#fff">Questions for Us?</h5>
<div class="abs inp" style="left:419px;top:1031px;width:111px;height:19px">Subject</div>
<div class="abs inp" style="left:539px;top:1031px;width:111px;height:19px">Email</div>
<div class="abs inp" style="left:419px;top:1058px;width:231px;height:58px;padding-top:7px">Message</div>
<div class="abs submit">Submit</div>

<div class="abs bottom"></div>
<div class="abs copy">© All Rights Reserved 2012</div>
<div class="abs social">Socialize With Us <i></i><i></i><i></i><i></i><i></i></div>
</body>
</html>
```